Business card design based on existing website

Please make a business card that is consistent with the look and feel of my new website: http://tellbury.com.sg. By going to the site, I think you'll have all you need in terms of the work I do and the colors I use.

I would like to ask the winner of this project to then do a separate project to design my stationery.

Target Market(s)

Heads of human resources, people wanting psychotherapy, and executives wanting coaching. (It's quite a mix!)

Industry/Entity Type

Psychology

Contact Information for Business Card

Email: ray5678@tellbury.com.sg
Website: http://tellbury.com.sg
Tel: +65 94706218

(I will not have a physical address on the card)

Font styles to use
Serif

Colors

Designer to choose colors to be used in the design.

Requirements
Must have
• On the Front
• ==========
• Have "Dr. Raymond Tellbury" using the font of the website.
• Also "Executive Coach, Psychotherapist, Leadership Professor"
• The back should mention
• ==================
• My degrees
• -------------
• "PhD Kelworth; Post Doc Drayfield". E.g., "Raymond Tellbury (PhD Kelworth; Post Doc Drayfield)" where the text between brackets was in smaller font.
• My work
• ----------
• "Executive coach, psychotherapist, and leadership professor"
• My job titles
• ---------------
• "Principal (Tellbury Consulting)
• Adjunct Professor (Lornvale Commerce University)
• Adjunct Associate Professor (Pemberly Institute of Letters)
• Coach & Supervisor (OKTRAV) '
• Options:
• 1) you can abbreviate Adjunct Professor to "Adj Prof" or "Adj Professor"; and "Adjunct Associate Professor" to "Adj Assoc Prof"
• 2) you abbreviate "Pemberly Institute of Letters" and "Lornvale Commerce University" to "PIL" and "LCU"
• 3) You can also combine the titles for PIL and LCU, e.g., "Adjunct faculty (PIL & LCU)
Nice to have
• Because I work with many Chinese people, it is sometimes helpful to have my family name, "Tellbury", in caps. In the past I have not used caps because it takes away from the aesthetic of the card. Only use caps if it looks good.
• The uploaded image of a "RT" is something that may be helpful. I am undecided.
• THANK YOU for helping me!
Should not have
• No photos. In my industry people consider it overselling.

```html
<!DOCTYPE html>
<html lang="en">
<head>
<meta charset="utf-8">
<title>Dr. Raymond Tellbury – Business Card</title>
<link rel="stylesheet" href="https://fonts.googleapis.com/css2?family=EB+Garamond:wght@400&family=PT+Sans+Narrow&display=swap">
<style>
  :root {
    --backdrop: #2b2b2b;
    --card-white: #ffffff;
    --forest: #1b2a1b;
    --ink: #1f2a1f;
    --cream: #f5f0c8;
  }
  * { margin: 0; padding: 0; box-sizing: border-box; }
  html, body { width: 1200px; height: 960px; overflow: hidden; }
  body { background: var(--backdrop); position: relative; font-family: "EB Garamond", Garamond, serif; }

  .card { position: absolute; width: 600px; height: 342px; }

  .card-front { left: 302px; top: 129px; background: var(--card-white); }
  .accent-bar { position: absolute; left: 0; top: 64px; width: 15px; height: 212px; background: var(--forest); }
  .front-name { position: absolute; left: 41px; top: 60px; font-size: 24px; color: var(--ink); line-height: 1; letter-spacing: 0.2px; }
  .degrees { position: absolute; left: 41px; top: 92px; font-family: "PT Sans Narrow", "Arial Narrow", sans-serif; font-size: 12.5px; color: var(--ink); line-height: 1; }
  .roles { position: absolute; left: 43px; top: 118px; font-size: 13.5px; line-height: 17.5px; color: var(--ink); }
  .contact { position: absolute; left: 44px; top: 207px; font-size: 13.5px; line-height: 18px; color: var(--ink); }

  .card-back { left: 299px; top: 488px; background: var(--forest); display: flex; align-items: center; justify-content: center; }
  .back-name { font-size: 46px; color: var(--cream); line-height: 1; letter-spacing: 0.2px; margin-top: 0; }
</style>
</head>
<body>
  <section class="card card-front">
    <div class="accent-bar"></div>
    <h1 class="front-name" style="font-weight:400">Dr. Raymond Tellbury</h1>
    <p class="degrees">(PhD Kelworth; Post Doc Drayfield)</p>
    <p class="roles">
      Executive coach, psychotherapist, and<br>
      leadership trainer Principal (Tellbury Consulting)<br>
      Adj Prof (LCU) Adj Assoc Prof(PIL)<br>
      Coach &amp; Supervisor (OKTRAV)
    </p>
    <p class="contact">
      +65 94706218<br>
      ray5678@tellbury.com.sg<br>
      www.tellbury.com.sg
    </p>
  </section>

  <section class="card card-back">
    <p class="back-name">Dr. Raymond Tellbury</p>
  </section>
</body>
</html>
```